Letterbox drop flyers for local business

I need a flyer design for my small business located in Canberra ACT called "Tallowbend Garden Care" My company is a landscaping business offering garden design, landscaping services, garden maintenance and horticultural services. I would like to have a flyer I can leave at nurseries and do letterbox drops with that highlight the professional quality of our services and also our brand feel of rural Australia and old fashioned vibe. The flyer should highlight our services and our "free quote" policy. Attached is my business logo.

Industry/Entity Type

Small Business

Font styles to use
Serif
Decorative

Colors
f37122
fcca95
ec1f27
abd036
9bcb3c

Requirements
Must have
• A list of our services and all my contact information as well as our offer for free quotes. Present this flyer and customer receives first hour of gardening free
Nice to have
• I would like the overall feel of the design to be old fashioned. Think old painted advertisments for wickam soap and brennicks biscuits, or an old dorvan pick-up truck with the dog in the back, want to highlight our quality but also give my customers a feel for our brand as a whole

```html
<!DOCTYPE html>
<html lang="en">
<head>
<meta charset="utf-8">
<title>Tallowbend Garden Care – Flyer</title>
<link href="https://fonts.googleapis.com/css2?family=Cinzel:wght@700&family=Roboto+Condensed:ital,wght@0,300;0,700;1,700&display=swap" rel="stylesheet">
<style>
  :root {
    --backdrop: #5c6069;
    --paper: #e4cfae;
    --paper-light: #eddcbf;
    --brand-red: #7a1a1c;
    --leaf-dark: #3c6a22;
    --leaf-lime: #abd036;
    --service-green: #4a6b23;
    --contact-green: #4f6b2e;
    --badge-brown: #5a3410;
    --badge-text: #d9e23a;
    --white: #ffffff;
  }
  * { margin: 0; padding: 0; box-sizing: border-box; }
  html, body { width: 1200px; height: 1000px; overflow: hidden; }
  body { background: var(--backdrop); position: relative; }

  .flyer {
    position: absolute; left: 278px; top: 40px;
    width: 644px; height: 910px;
    background: var(--white);
    overflow: hidden;
  }
  .flyer__header {
    position: absolute; left: 0; top: 0; width: 644px; height: 470px;
    background: radial-gradient(ellipse at 50% 30%, var(--paper-light), var(--paper));
  }
  .brand-name {
    position: absolute; left: 0; width: 100%; text-align: center;
    font-family: "Cinzel", serif; font-weight: 700; color: var(--brand-red);
    line-height: 1;
  }
  .brand-name--main { top: 112px; font-size: 76px; letter-spacing: 1px; }
  .brand-name--sub { top: 212px; font-size: 46px; }

  .offer {
    position: absolute; left: 0; top: 292px; width: 100%; text-align: center;
    font-family: "Cinzel", serif; font-weight: 700; font-size: 14px;
    line-height: 18px; color: var(--brand-red); letter-spacing: 0.5px;
  }

  .services {
    position: absolute; left: 0; top: 360px; width: 100%; text-align: center;
    font-family: "Cinzel", serif; font-weight: 700; font-size: 17px;
    line-height: 22px; color: var(--service-green); letter-spacing: 0.5px;
  }

  .garden-photo {
    position: absolute; left: 0; top: 440px; width: 644px; height: 305px;
    background: linear-gradient(180deg, #2f5a22 0%, #3f7a2a 45%, #5da73a 80%, #7cc043 100%);
  }
  .garden-wave { position: absolute; left: 0; top: 425px; width: 644px; height: 70px; }

  .flyer__footer {
    position: absolute; left: 0; top: 745px; width: 644px; height: 165px;
    background: linear-gradient(180deg, #e9eaea 0%, var(--white) 30%);
  }

  .quote-badge { position: absolute; left: 242px; top: 638px; width: 160px; height: 160px; }
  .quote-badge__small { font-family: "Roboto Condensed", sans-serif; font-style: italic; font-weight: 700; font-size: 12px; fill: var(--badge-text); }
  .quote-badge__big { font-family: "Roboto Condensed", sans-serif; font-weight: 700; font-size: 50px; fill: var(--badge-text); }
  .quote-badge__mid { font-family: "Roboto Condensed", sans-serif; font-style: italic; font-weight: 700; font-size: 26px; fill: var(--badge-text); }

  .contact {
    position: absolute; left: 0; width: 100%; text-align: center;
    font-family: "Roboto Condensed", sans-serif; color: var(--contact-green);
    line-height: 1.2;
  }
  .contact--tel { top: 797px; font-size: 27px; font-weight: 300; }
  .contact--web { top: 832px; font-size: 29px; font-weight: 300; }
  .contact--web strong { font-weight: 700; }
  .contact--abn { top: 869px; font-size: 8px; font-weight: 700; color: #333; }
</style>
</head>
<body>
  <main class="flyer">
    <section class="flyer__header">
      <div class="brand-name brand-name--main">Tallowbend</div>
      <div class="brand-name brand-name--sub">Garden Care</div>
      <p class="offer">Present this flyer and receive your<br>first hour of gardening free</p>
      <p class="services">GARDEN DESIGN, LANDSCAPING SERVICES<br>GARDEN MAINTENANCE &amp; HORTICULTURAL SERVICES</p>
    </section>

    <div class="garden-photo" role="img" aria-label="Photograph of a landscaped garden with lawn, flowering beds, shrubs and garden lamps"></div>

    <svg class="garden-wave" viewBox="0 0 644 70" preserveAspectRatio="none" aria-hidden="true">
      <path d="M0 0 H644 V48 C520 30 420 20 300 22 C180 24 80 20 0 18 Z" fill="var(--paper)"/>
      <path d="M0 18 C80 20 180 24 300 22 C420 20 520 30 644 48 L644 56 C520 40 420 32 300 34 C180 36 80 30 0 30 Z" fill="var(--leaf-dark)"/>
      <path d="M0 30 C80 30 180 36 300 34 C420 32 520 40 644 56 L644 62 C520 48 420 40 300 42 C180 44 80 38 0 36 Z" fill="var(--leaf-lime)"/>
    </svg>

    <section class="flyer__footer"></section>

    <svg class="quote-badge" viewBox="0 0 160 160" aria-label="Call us for your free quote">
      <polygon fill="var(--badge-brown)" stroke="#3a2008" stroke-width="2" points="80,2 88,16 101,5 105,21 120,13 120,30 136,27 131,43 148,45 139,58 155,65 142,75 156,85 140,93 151,106 134,109 140,125 123,124 125,141 109,136 106,152 93,143 86,158 80,146 74,158 67,143 54,152 51,136 35,141 37,124 20,125 26,109 9,106 20,93 4,85 18,75 5,65 21,58 12,45 29,43 24,27 40,30 40,13 55,21 59,5 72,16"/>
      <text class="quote-badge__small" x="80" y="46" text-anchor="middle">Call Us For Your</text>
      <text class="quote-badge__big" x="80" y="94" text-anchor="middle">FREE</text>
      <text class="quote-badge__mid" x="80" y="122" text-anchor="middle">QUOTE</text>
    </svg>

    <p class="contact contact--tel">TEL: 04 5512 8047</p>
    <p class="contact contact--web">Leafpage.com/<strong>TallowbendGardensACT</strong></p>
    <p class="contact contact--abn">ABN: 61 905 337 204</p>
  </main>
</body>
</html>
```